Coralvale Jukebox and Jumping Castle Hire

Hi folks,
This is for a new business based in CORALVALE(Australia), the business hires, jukeboxes, inflatable games(mostly jumping castles) and slushy/cocktail machines.
I want the website to appeal to people looking to party. Does that sound too simplistic?
It should be simple to navigate, I require only the front page but make it easy to get to the rest of the site.
Modern, exciting and funky, think rock band or concert promoter.
We are trying to sell packages of products, there should be several packages visible on the front page without looking cluttered.
Link to jukebox song list.
Friendlane, pondlet etc.
I am currently on holidays so I have a fair amount of time to get this project done, it says 10 days I hope to have it done much sooner.

Reason: So far there is no design that I am happy with. I am after a website for Jukeboxes, it should have a rock concert feel.

Ages 20 to 50

Business

• Think rock band type website, black with bold color highlight.
• Plain or bland color.
Pictures of CORALVALE or any other city.
Vexaro map or any other location type map.

```html
<!DOCTYPE html>
<html lang="en">
<head>
<meta charset="utf-8">
<title>Coralvale Jukebox and Jumping Castle Hire</title>
<link href="https://fonts.googleapis.com/css2?family=Open+Sans:wght@400;600;700;800&display=swap" rel="stylesheet">
<style>
:root{
  --red:#f2411f;
  --bg:#0c0c0c;
  --bar:#1a1a1a;
  --nav:#1f1f1f;
  --card:#151515;
  --text:#c9c9c9;
  --muted:#8a8a8a;
  --dim:#555;
  --white:#fff;
}
*{margin:0;padding:0;box-sizing:border-box}
html,body{width:1200px;height:2164px;overflow:hidden;background:var(--bg);font-family:'Open Sans',Arial,sans-serif;color:var(--text)}
.page{position:relative;width:1200px;height:2164px}
.abs{position:absolute}
.topbar{left:0;top:0;width:1200px;height:45px;background:var(--bar)}
.contact-line{font-size:11px;color:#d8d8d8;display:flex;gap:20px;align-items:center}
.contact-line span{display:flex;align-items:center;gap:7px}
.search{left:865px;top:8px;width:153px;height:29px;background:#050505}
.navbar{left:0;top:45px;width:1200px;height:80px;background:var(--nav)}
.nav-rule{left:0;top:125px;width:1200px;height:5px;background:#5a5a5a}
.logo{left:186px;top:60px}
.logo .name{font-size:25px;font-weight:800;color:var(--white);letter-spacing:1px;line-height:1}
.logo .tag{font-size:8.5px;color:#ddd;margin-top:3px;font-weight:600}
.menu a{position:absolute;top:0;height:80px;line-height:80px;font-size:11.5px;font-weight:700;color:var(--white);text-decoration:none;text-transform:uppercase;text-align:center;transform:translateX(-50%);padding:0 18px}
.menu a.active{background:#2b2b2b;color:var(--red)}
.hero{left:0;top:130px;width:1200px;height:527px;background:radial-gradient(ellipse at 55% 30%,#4a423c 0%,#2b2622 40%,#0d0c0b 100%)}
.jukebox{left:203px;top:213px;width:210px;height:316px;background:linear-gradient(160deg,#5a4636,#2a211b);border-radius:6px}
.hero-copy{left:474px;top:310px}
.hero-copy h1{font-size:56px;font-weight:700;color:var(--white);line-height:1.1}
.hero-copy h1 em{font-style:normal;color:var(--red)}
.hero-copy h2{font-size:45px;font-weight:400;color:var(--white);line-height:1.15}
.hero-copy h2 b{font-weight:700}
.hero-copy p{font-size:19px;color:var(--red);margin-top:4px}
.dot{width:15px;height:15px;border-radius:50%;background:#bbb;border:3px solid #333}
.player{left:0;top:657px;width:1200px;height:55px;background:#1c1c1c;border-top:1px solid #2a2a2a;border-bottom:1px solid #2a2a2a}
.track{left:308px;top:669px;font-size:12px;font-weight:700;color:#ddd}
.track span{font-weight:400;color:#666}
.progress{left:308px;top:690px;width:621px;height:8px;background:#333}
.progress i{display:block;width:171px;height:8px;background:var(--red)}
.volume{left:968px;top:690px;width:50px;height:8px;background:#333}
.section-title{font-size:22px;font-weight:700;color:var(--white)}
.section-title em{font-style:normal;color:var(--red)}
.intro{left:183px;top:785px;width:200px}
.castle{width:66px;height:84px;background:linear-gradient(#cfcfcf,#9a9a9a)}
.intro p{font-size:12px;line-height:20px;color:#aaa;margin-top:8px}
.link-red{font-size:10px;color:var(--red);text-transform:uppercase}
.card{width:196px;background:var(--card)}
.card .img{height:195px}
.card .cap{padding:9px 11px 10px}
.card h3{font-size:12.5px;font-weight:700;color:var(--red);line-height:17px}
.quote{font-size:10px;color:#777;margin-top:6px;display:flex;align-items:center;gap:7px}
.quote i{display:inline-block;width:10px;height:10px;border:1px solid #666}
.rule{height:1px;background:#262626}
.about-photo{left:183px;top:1513px;width:551px;height:221px;background:linear-gradient(120deg,#6b4a55,#3a2f3a 45%,#7a5a3a)}
.about-text{left:183px;top:1760px;width:551px;font-size:12px;line-height:20px;color:#bbb}
.about-text p{margin-bottom:16px}
.side{left:752px;width:266px}
.side h4{font-size:14px;font-weight:700;color:var(--white)}
.event{display:flex;align-items:flex-start;gap:9px;font-size:12px;color:#ccc;line-height:17px;margin-top:15px}
.event .date{background:var(--red);color:var(--white);font-weight:700;font-size:11px;padding:0 4px;flex:none}
.tweet{font-size:11px;line-height:18px;color:#aaa}
.tweet small{display:block;font-style:italic;color:#666;font-size:10px;margin-top:4px}
.footer-band{left:0;top:1992px;width:1200px;height:30px;background:#151515}
.social{left:830px;top:1999px;display:flex;gap:11px}
.social i{display:block;width:16px;height:16px;background:#4a4a4a;border-radius:2px}
.footer{left:0;top:2022px;width:1200px;height:142px;background:#111}
.footer-nav{left:183px;top:2078px;display:flex;font-size:10px;color:#888;text-transform:uppercase}
.footer-nav a{color:#888;text-decoration:none;padding:0 14px;border-left:1px solid #333}
.footer-nav a:first-child{padding-left:0;border:0}
.copyright{left:183px;top:2120px;font-size:8px;color:#3a3a3a;text-transform:uppercase}
</style>
</head>
<body>
<div class="page">

  <div class="abs topbar"></div>
  <div class="abs contact-line" style="left:186px;top:14px">
    <span><svg width="11" height="11" viewBox="0 0 12 12"><rect width="12" height="12" rx="2" fill="#ccc"/><path d="M3.5 2.5l1.5 1.6-.8 1c.6 1.3 1.4 2.1 2.7 2.7l1-.8 1.6 1.5-1 1.3C5.6 9.600 2.400 6.400 2.2 3.500z" fill="#1a1a1a"/></svg>07 5550 1842</span>
    <span><svg width="12" height="9" viewBox="0 0 12 9"><rect width="12" height="9" fill="#ccc"/><path d="M0 0l6 5 6-5" stroke="#1a1a1a" fill="none"/></svg>info@coralvalejukeboxhire.com</span>
  </div>
  <div class="abs search"><svg class="abs" style="right:9px;top:9px" width="11" height="11" viewBox="0 0 11 11"><circle cx="4.5" cy="4.5" r="3.5" stroke="#666" stroke-width="1.5" fill="none"/><path d="M7 7l3 3" stroke="#666" stroke-width="1.5"/></svg></div>

  <div class="abs navbar">
    <nav class="menu">
      <a class="active" style="left:400px">Home</a>
      <a style="left:484px">Jukeboxes</a>
      <a style="left:609px">Inflatable Games</a>
      <a style="left:757px">Cocktail Machines</a>
      <a style="left:880px">Packages</a>
      <a style="left:973px">Contact</a>
    </nav>
  </div>
  <div class="abs logo"><div class="name">CORALVALE</div><div class="tag">Jukebox and Jumping Castle Hire</div></div>
  <div class="abs nav-rule"></div>

  <section class="abs hero" role="img" aria-label="Concert crowd with raised hands under stage lights"></section>
  <div class="abs jukebox" role="img" aria-label="Modern touchscreen wall jukebox"></div>
  <div class="abs hero-copy">
    <h1>Liven Up <em>Your Party</em></h1>
    <h2>State of the art <b>Jukeboxes</b></h2>
    <p>Choose from our wide collection or create your own playlist</p>
  </div>
  <svg class="abs" style="left:28px;top:378px" width="14" height="22" viewBox="0 0 14 22"><path d="M11 2L3 11l8 9" stroke="#fff" stroke-width="3" fill="none"/></svg>
  <svg class="abs" style="left:1158px;top:378px" width="14" height="22" viewBox="0 0 14 22"><path d="M3 2l8 9-8 9" stroke="#fff" stroke-width="3" fill="none"/></svg>
  <div class="abs dot" style="left:573px;top:621px"></div>
  <div class="abs dot" style="left:593px;top:621px"></div>
  <div class="abs dot" style="left:613px;top:621px"></div>

  <div class="abs player"></div>
  <svg class="abs" style="left:182px;top:674px" width="110" height="20" viewBox="0 0 110 20">
    <path d="M14 5v10l-6-5zM8 5v10L2 10z" fill="#999"/>
    <path d="M30 2v16l13-8z" fill="#bbb"/>
    <path d="M62 5v10l6-5zM68 5v10l6-5z" fill="#999"/>
    <path d="M90 5h11M90 10h11M90 15h11" stroke="#999" stroke-width="2"/>
  </svg>
  <div class="abs track">Something Bright - Milo Harrow <span>(01:05/03:42)</span></div>
  <div class="abs progress"><i></i></div>
  <svg class="abs" style="left:945px;top:687px" width="16" height="14" viewBox="0 0 16 14"><path d="M1 5h3l4-4v12L4 9H1z" fill="#777"/><path d="M11 4c1.500 1.500 1.500 4.500 0 6" stroke="#777" fill="none"/></svg>
  <div class="abs volume"></div>

  <div class="abs intro">
    <div class="castle" role="img" aria-label="Castle icon with music note"></div>
    <div class="section-title" style="margin-top:10px">Our <em>Products.</em></div>
    <p>Lorem ipsum dolor sit amet, con sectetuer adipiscing elit.</p>
    <div class="link-red" style="margin-top:32px">- View all</div>
  </div>

  <div class="abs card" style="left:396px;top:785px"><div class="img" role="img" aria-label="Guest choosing songs on a touchscreen jukebox" style="background:linear-gradient(135deg,#3a4a7a,#8a6a9a 60%,#c89a7a)"></div><div class="cap"><h3>Jukeboxes</h3><div class="quote"><i></i>Get A Quote</div></div></div>
  <div class="abs card" style="left:609px;top:785px"><div class="img" role="img" aria-label="Kids playing on a bright inflatable game" style="background:linear-gradient(135deg,#e0c020,#e07020 50%,#3a6ac0)"></div><div class="cap"><h3>Inflatable Games</h3><div class="quote"><i></i>Get A Quote</div></div></div>
  <div class="abs card" style="left:824px;top:785px"><div class="img" role="img" aria-label="Cocktail being poured from a slushy machine" style="background:linear-gradient(160deg,#c02020,#5a1010 55%,#1a0a0a)"></div><div class="cap"><h3>Cocktail Machines</h3><div class="quote"><i></i>Get A Quote</div></div></div>

  <div class="abs section-title" style="left:183px;top:1099px">Our <em>Packages.</em></div>
  <svg class="abs" style="left:980px;top:1106px" width="40" height="16" viewBox="0 0 40 16"><path d="M9 2L3 8l6 6M31 2l6 6-6 6" stroke="#fff" stroke-width="2.5" fill="none"/></svg>

  <div class="abs card" style="left:183px;top:1148px"><div class="img" role="img" aria-label="Jukebox beside a cocktail machine" style="background:linear-gradient(180deg,#3a3a3a,#2a2a2a)"></div><div class="cap"><h3>Jukebox &amp; Cocktail<br>Machine</h3><div class="quote"><i></i>Get A Quote</div></div></div>
  <div class="abs card" style="left:396px;top:1148px"><div class="img" role="img" aria-label="Jumping castle with a jukebox" style="background:linear-gradient(90deg,#3a3a3a,#4a5a8a 50%,#3a3a3a)"></div><div class="cap"><h3>Jukebox &amp; Jumping Castle</h3><div class="quote"><i></i>Get A Quote</div></div></div>
  <div class="abs card" style="left:609px;top:1148px"><div class="img" role="img" aria-label="Jukebox, cocktail machine and jumping castle together" style="background:linear-gradient(90deg,#3a3a3a,#5a6a4a 50%,#3a3a3a)"></div><div class="cap"><h3>Jukebox, Cocktail Machine<br>&amp; Jumping Castle</h3><div class="quote"><i></i>Get A Quote</div></div></div>
  <div class="abs card" style="left:824px;top:1148px"><div class="img" role="img" aria-label="Cocktail machine with a jumping castle" style="background:linear-gradient(90deg,#3a3a3a,#8a7a3a 50%,#3a3a3a)"></div><div class="cap"><h3>Cocktail Machine &amp;<br>Jumping Castle</h3><div class="quote"><i></i>Get A Quote</div></div></div>

  <div class="abs rule" style="left:183px;top:1484px;width:551px"></div>
  <div class="abs rule" style="left:752px;top:1484px;width:266px"></div>

  <div class="abs about-photo" role="img" aria-label="Friends celebrating at a party"></div>
  <div class="abs about-text">
    <p>Lorem ipsum dolor sit amet, consectetuer adipiscing elit, sed diam nonummy nibh euismod tinci dunt ut laoreet dolore magna aliquam erat volutpat. Ut wisi enim ad minim veniam, quis nostrud exerci tation ullamcorper suscipit lobortis possim assum.</p>
    <p>Typi non habent claritatem insitam est usus legentis in iis qui facit eorum claritatem. Investigationes demonstraverunt lectores legere me lius quod ii legunt saepius. Claritas est etiam processus dyna micus, qui sequitur mutationem consuetudium lectorum.</p>
    <div class="link-red" style="margin-top:20px">- More about us</div>
  </div>

  <div class="abs side" style="top:1513px">
    <h4>Events</h4>
    <div class="event"><span class="date">12/08/14</span>Nam liber tempor - claritatem</div>
    <div class="event"><span class="date">12/08/14</span>Typi non habent</div>
    <div class="event"><span class="date">12/08/14</span>Claritas est etiam et</div>
    <div class="event"><span class="date">12/08/14</span>Duis autem vel eum iriure dolor in hendrerit.</div>
  </div>
  <div class="abs side" style="top:1730px">
    <h4 style="font-size:12px">Pondlet feed.</h4>
    <div class="rule" style="margin-top:8px;background:#333"></div>
    <div class="tweet" style="margin-top:12px">Ut wisi enim ad minim veniam, quis nostrud exerci tation ullam corper suscipit lobortis nis.<small>2 days ago</small></div>
    <div class="tweet" style="margin-top:8px;color:#555">...</div>
    <div class="tweet" style="margin-top:4px">Anteposuerit litterarum formas humanitatis per seacula quarta decima et quinta decima. Modo typi, qui nunc nobis videntur parum clari,<small>3 days ago</small></div>
  </div>

  <div class="abs footer-band"></div>
  <div class="abs contact-line" style="left:183px;top:2001px;color:#999">
    <span><svg width="11" height="11" viewBox="0 0 12 12"><rect width="12" height="12" rx="2" fill="#888"/><path d="M3.5 2.5l1.5 1.6-.8 1c.6 1.3 1.4 2.1 2.7 2.7l1-.8 1.6 1.5-1 1.3C5.600 9.600 2.400 6.400 2.200 3.500z" fill="#151515"/></svg>07 5550 1842</span>
    <span><svg width="12" height="9" viewBox="0 0 12 9"><rect width="12" height="9" fill="#888"/><path d="M0 0l6 5 6-5" stroke="#151515" fill="none"/></svg>info@coralvalejukeboxhire.com</span>
  </div>
  <div class="abs social"><i></i><i></i><i></i><i></i><i></i><i></i><i></i></div>

  <div class="abs footer"></div>
  <nav class="abs footer-nav"><a>Home</a><a>Products</a><a>Packages</a><a>Blog</a><a>Contact</a></nav>
  <div class="abs copyright">Copyright © 2014 Coralvale Jukebox. All rights reserved.</div>

</div>
</body>
</html>
```